Wordpress Design Project - Vibrant Children's school bag website

We need a fresh design for the landing page of our new web site and blog: tumblewickshop.com

Tumblewick specialises in supplying schools all over the world and now also parents directly with, personalised school bags, accessories, crafts and gifts for their children.

I have attached the visual that our web designers have provided so that we can see the layout of the various window, but now we need to add the personal touch of making it our own and visually making the site look enticing and exciting to shop on.

Hello Designers,

We are now in the final round of choosing a design.  We have found that most deisgns are very similar and that none are completley original.  Therefore, we are willing to throw our wire frame away and start with a compleltely new visual so you can design what ever you like!

The only requirements we have is that we must have:
- A large rolling banner to show our products lines
- Our Company logo
- Meta going tags across the top
- Icons for facebook,pintrest,blog,
- Account Login bar
- A log in area for schools
- A login area to register for the Club Tumbo

So we are looking for something that really stands out from the crowd!

can you deliver?

Thanks,

Target Market(s)

To appeal to mum's shopping on line for their children's school items and gifts.

Industry/Entity Type

School

Requirements
Must have
• -When you see the visual attached please note the amendments:
- the word 'school bags' under our company name will not appear
- the tag line "Australia's no 1 specialist school bag company' should be deleted. We will leave this area open so that you can include some simple icons that we would like featured across the top of the banner i.e:
- a love heart icon + wording to say : Made with love
- A 'delivery' icon + wording to say : Free delivery
- A 'warranty' icon + wording to say : up to 25 year warranty
- A 'world' icon + wording to say : we ship to the universe
(Please see: www.plumcottage.com.au for reference of what we mean!)

We we want the overall design to be clean, fresh, crisp and fun to look at.

You may alter the colours of everything, even the coloured tabs. we think that the coloured tabs should actually just be one colour through out and to let the tumblewick name stand out with all it's.

The top/main photo will be a rolling banner.

You can change the shapes of the boxes but keep to the wire frame.

Please alter the design of the black/coloured club tumbo card to suit your design.

Our aim is to also change the side panels in peak seasons to reflect halloween banner, christmas banner etc.

Please see my screen shot of the current page and see where the "dots' pattern sits on either side of the shopping panels. Please include the side panels as we want to change the design to have themes i.e for halloween, for christmas etc etc.

example of websites that have this:

http://www.reefmarlo.com/

Please include a 'blog' and pintrest icon.

The site will not only manage our retail sales but will also be a portal for our schools to register and place their bulk orders with us. So the "wholesale register box" must stand out so our school customers can easily see where they need to click & register.
Should not have
• Please do not do a 'baby' boutique theme. We need a theme that appeals to mum's that have children across the ages of 3-14 years.

```html
<!DOCTYPE html>
<html lang="en">
<head>
<meta charset="utf-8">
<title>Tumblewick – Kids School Bags &amp; Accessories</title>
<link rel="stylesheet" href="https://fonts.googleapis.com/css2?family=Alegreya:wght@400;700&family=Questrial&family=Rosario:wght@400&family=Open+Sans:wght@400;600&family=Fredoka:wght@600&display=swap">
<style>
:root{
  --grid-bg:#fbfbfb;
  --grid-line:#ececec;
  --paper:#f4ecdc;
  --paper-dark:#e6d9bf;
  --cocoa:#2a1c10;
  --cocoa-mid:#5b5045;
  --nav-grey:#7d746a;
  --nav-text:#f7f2ea;
  --frame:#c9a77a;
  --brown-text:#6b4a2b;
  --body-text:#4a4a4a;
  --red:#e3141b;
  --link-blue:#2a7fc2;
  --link-red:#e3141b;
  --yellow:#f5d70c;
  --sale-pink:#d84fd0;
  --buy-green:#9bd43b;
  --login-yellow:#f2e50e;
}
*{box-sizing:border-box;margin:0;padding:0}
html,body{width:1200px;height:1018px;overflow:hidden}
body{
  position:relative;
  background-color:var(--grid-bg);
  background-image:linear-gradient(var(--grid-line) 1px,transparent 1px),linear-gradient(90deg,var(--grid-line) 1px,transparent 1px);
  background-size:18px 18px;
  font-family:"Questrial",sans-serif;
  color:var(--body-text);
}
.abs{position:absolute}

/* Header */
.masthead{left:138px;top:0;width:734px;height:138px;background:linear-gradient(180deg,#f6efe1,var(--paper));}
.brand{left:12px;top:20px;display:flex;align-items:center;gap:10px;font-family:"Fredoka",sans-serif;font-weight:600;font-size:52px;color:#1b9ad6;letter-spacing:-1px}
.brand-dot{width:16px;height:16px;border-radius:50%;background:#8a2b9c}
.social-row{right:16px;top:11px;display:flex;gap:5px}
.social-row span{width:24px;height:24px;border-radius:4px;display:block}
.perks{left:250px;top:76px;display:flex;gap:22px;align-items:center}
.perk{display:flex;align-items:center;gap:5px;font-family:"Open Sans",sans-serif;font-size:11px;line-height:12px;color:#666}
.perk b{display:block;color:#333;font-size:13px}

/* Side navigation */
.side-nav{left:872px;top:0;width:185px;height:554px;background:var(--cocoa);padding:4px 0 0 4px;list-style:none}
.side-nav li{display:flex;height:39px;margin-bottom:3.5px;align-items:center}
.side-nav .tab{width:40px;height:39px;background:linear-gradient(135deg,#f1e4cc,#d9c3a0);display:flex;align-items:center;justify-content:center}
.side-nav .label{flex:1;height:39px;line-height:39px;padding-left:14px;background:linear-gradient(90deg,#8d857d,var(--nav-grey) 40%,#5e554c);color:var(--nav-text);font-family:"Rosario",sans-serif;font-size:16px}
.side-nav .login .tab{background:var(--login-yellow)}
.side-nav .sale .tab{background:var(--sale-pink)}
.side-nav .buy .tab{background:var(--buy-green)}

/* Slider */
.slide{top:150px;width:337px;height:401px;background:var(--frame);padding:7px;box-shadow:0 1px 3px rgba(0,0,0,.3)}
.slide .photo{width:100%;height:100%;background:#fff}
.slide .tag{position:absolute;left:7px;top:4px;background:var(--cocoa);color:#fff;font-size:14px;padding:2px 10px;min-width:124px}
.slide .more{position:absolute;right:7px;bottom:4px;background:var(--cocoa);color:#fff;font-size:12px;padding:3px 8px}
.arrow{top:305px}
.rule{height:1px;background:#999}

/* About */
.about{left:120px;top:567px;width:635px;height:188px;background:#f4f3f1;box-shadow:0 1px 2px rgba(0,0,0,.2)}
.about-tab{left:120px;top:567px;width:203px;height:38px;background:var(--cocoa);color:#f3e3c0;font-family:"Alegreya",serif;font-size:25px;padding-left:46px;line-height:38px}
.about h2{position:absolute;left:40px;top:51px;font-family:"Alegreya",serif;font-weight:700;font-size:17px;color:var(--brown-text)}
.about p{position:absolute;left:54px;top:78px;width:560px;font-size:14px;line-height:21px;color:#444}
.about .more-link{position:absolute;right:24px;bottom:10px;font-size:14px;color:#333;display:flex;align-items:center;gap:4px}

/* Club */
.club{left:767px;top:567px;width:287px;height:185px;background:linear-gradient(180deg,#f4efe7,#ebe4d8);box-shadow:0 1px 2px rgba(0,0,0,.2);overflow:hidden}
.club h3{text-align:center;margin-top:8px;font-family:"Alegreya",serif;font-weight:700;font-size:21px;color:#222}
.club .offer{margin:2px 8px 0;background:var(--red);color:#fff;font-size:17px;height:36px;line-height:32px;padding-left:22px}
.field{background:#fff;border:2px solid #cfcac2;border-radius:7px;font-size:13px;color:#222}
.club .field{position:absolute;left:18px;top:88px;width:186px;height:26px;line-height:22px;padding-left:40px}
.club .btn{position:absolute;left:103px;top:122px;width:80px;height:22px;border:1px solid #bbb;border-radius:11px;background:#fff;text-align:center;font-size:13px;line-height:20px}
.small{font-family:"Open Sans",sans-serif;font-size:10px;color:#333;line-height:13px}
.small .red{color:var(--link-red)}
.small .blue{color:var(--link-blue)}
.club .small{position:absolute;left:64px;top:150px}

/* Bottom row */
.panel-title{font-family:"Alegreya",serif;font-size:27px;text-align:center}
.endorse{left:139px;top:775px;width:288px;height:185px;background:#eae5df;padding:8px}
.endorse .inner{width:100%;height:100%;background:#f8f7f5;position:relative}
.endorse .panel-title{padding-top:2px;padding-left:36px;color:#222}
.endorse .portrait{position:absolute;left:7px;top:32px;width:68px;height:88px;border:3px solid #fff;box-shadow:0 0 2px #999;background:linear-gradient(180deg,#d8dde0,#b8a89a)}
.endorse .who{position:absolute;left:84px;top:34px}
.endorse .who b{display:block;font-weight:400;color:var(--link-blue);font-size:14px}
.endorse .who i{font-style:normal;color:var(--brown-text);font-size:13px}
.endorse .quote{position:absolute;left:81px;top:73px;width:192px;font-family:"Open Sans",sans-serif;font-size:9.5px;line-height:11px;color:#333}
.endorse .go{position:absolute;right:12px;bottom:26px;width:12px;height:12px;border-radius:50%;background:#e0641c}
.social{left:455px;top:781px;width:275px;height:171px;background:radial-gradient(ellipse at 45% 30%,#7aa0a0,#233 55%,#000);}
.social .panel-title{color:#fff;padding-top:6px}
.social svg{position:absolute;left:28px;top:52px}
.schools{left:768px;top:775px;width:287px;height:185px;background:#f0ebe3;padding:6px}
.schools .inner{width:100%;height:100%;position:relative;background:radial-gradient(ellipse at 30% 40%,#fff7b0,var(--yellow) 60%,#f0c800)}
.schools .panel-title{color:#231a10;padding-top:3px}
.schools .field{position:absolute;left:19px;top:44px;width:224px;height:36px;border-radius:9px;text-align:center;line-height:32px;font-size:15px;box-shadow:0 2px 3px rgba(0,0,0,.2)}
.schools .btn{position:absolute;left:32px;top:92px;width:98px;height:25px;border-radius:6px;background:linear-gradient(#ff3a44,#d6101a);color:#fff;text-align:center;line-height:25px;font-size:14px}
.schools .small{position:absolute;left:30px;top:127px}
.schools svg{position:absolute;left:170px;top:0}

/* Footer */
.site-footer{left:159px;top:978px;width:881px;height:40px;background:var(--cocoa);padding:5px 0 0 50px;font-family:"Open Sans",sans-serif;font-size:10.5px;color:#f0d86a;line-height:19px}
.site-footer .copy{color:#f4eee0}
</style>
</head>
<body>

<header class="abs masthead">
  <div class="abs brand"><span>tumblewick</span><span class="brand-dot"></span></div>
  <div class="abs social-row" aria-label="Social links">
    <span style="background:#3b5b9a"></span><span style="background:#3fa6dd"></span><span style="background:#c4302b"></span><span style="background:#c8232c"></span>
  </div>
  <div class="abs perks">
    <div class="perk">
      <svg width="22" height="20" viewBox="0 0 22 20"><path d="M11 18 C2 11 0 7 3 3.5 C6 0.5 9.5 2 11 5 C12.5 2 16 .5 19 3.5 C22 7 20 11 11 18Z" fill="none" stroke="#7a2b2b" stroke-width="1.6"/></svg>
      <span style="font-family:'Alegreya',serif;font-size:13px;color:#333">Made with Love</span>
    </div>
    <div class="perk">
      <svg width="56" height="34" viewBox="0 0 56 34"><rect x="1" y="6" width="32" height="20" fill="#111"/><path d="M34 12h12l8 8v6H34z" fill="#111"/><path d="M38 14h7l5 5H38z" fill="#eee"/><circle cx="10" cy="28" r="5" fill="#222" stroke="#e8d400" stroke-width="2"/><circle cx="43" cy="28" r="5" fill="#222" stroke="#e8d400" stroke-width="2"/></svg>
      <span><b>free</b>Delivery</span>
    </div>
    <div class="perk">
      <svg width="40" height="40" viewBox="0 0 40 40"><circle cx="20" cy="20" r="19" fill="#111" stroke="#e8d400" stroke-width="3"/><text x="20" y="28" text-anchor="middle" font-family="Alegreya,serif" font-size="22" fill="#fff">25</text></svg>
      <span><b style="font-family:'Alegreya',serif;font-size:15px">Years</b>Warranty</span>
    </div>
    <div class="perk">
      <svg width="44" height="40" viewBox="0 0 44 40"><circle cx="22" cy="20" r="18" fill="none" stroke="#111" stroke-width="2.5"/><ellipse cx="22" cy="20" rx="8" ry="18" fill="none" stroke="#111" stroke-width="2"/><path d="M4 20h36M7 11h30M7 29h30" stroke="#111" stroke-width="2"/><path d="M2 30 Q20 42 42 26" fill="none" stroke="#e8d400" stroke-width="3"/></svg>
      <span style="margin-top:-14px"><b style="font-weight:400;font-family:'Alegreya',serif">We Ship</b></span>
    </div>
  </div>
</header>

<nav>
<ul class="abs side-nav">
  <li class="login"><span class="tab"><svg width="24" height="24" viewBox="0 0 24 24"><path d="M7 6a8 8 0 1 0 10 0" fill="none" stroke="#222" stroke-width="3"/><path d="M12 2v9" stroke="#222" stroke-width="3"/></svg></span><span class="label">Account Login</span></li>
  <li><span class="tab"><svg width="22" height="20" viewBox="0 0 22 20"><path d="M11 1 1 10h3v9h5v-6h4v6h5v-9h3z" fill="#2a1c10"/></svg></span><span class="label">Home</span></li>
  <li><span class="tab"></span><span class="label">Kids Backpacks</span></li>
  <li><span class="tab"></span><span class="label">Kids Bags</span></li>
  <li><span class="tab"></span><span class="label">Sports</span></li>
  <li><span class="tab"></span><span class="label">Arts &amp; Crafts</span></li>
  <li><span class="tab"></span><span class="label">Kids Clothing</span></li>
  <li><span class="tab"></span><span class="label">Music</span></li>
  <li><span class="tab"></span><span class="label">Kids Diaries</span></li>
  <li><span class="tab"></span><span class="label">Kids Storage</span></li>
  <li><span class="tab"></span><span class="label">Extra Stuff</span></li>
  <li class="sale"><span class="tab"></span><span class="label">Sale</span></li>
  <li class="buy"><span class="tab"><svg width="24" height="20" viewBox="0 0 24 20"><path d="M1 2h4l3 11h12l3-8H7" fill="none" stroke="#2a4a10" stroke-width="2"/><circle cx="10" cy="17" r="2" fill="#2a4a10"/><circle cx="18" cy="17" r="2" fill="#2a4a10"/></svg></span><span class="label">Buy Items</span></li>
</ul>
</nav>

<section aria-label="Product banner">
  <svg class="abs arrow" style="left:143px" width="20" height="70" viewBox="0 0 20 70"><path d="M18 0 2 35 18 70 12 35z" fill="#a9a29a"/></svg>
  <div class="abs slide" style="left:166px">
    <div class="photo" role="img" aria-label="Dark blue school backpack packed with books, pencils and an apple" style="background:radial-gradient(ellipse at 50% 55%,#2b3d4a,#4b6f84 35%,#f6f6f6 70%)"></div>
    <span class="tag">Kids Backpacks</span>
    <span class="more">Click here to view More &nbsp;collection ▸</span>
  </div>
  <div class="abs slide" style="left:510px">
    <div class="photo" role="img" aria-label="Red pencil case, pens in a mesh holder, scissors and a calculator" style="background:radial-gradient(ellipse at 35% 65%,#d8203a,#e85466 25%,#c9ccd0 45%,#f7f7f7 72%)"></div>
    <span class="tag">Accessories</span>
    <span class="more">Click here to view More &nbsp;collection ▸</span>
  </div>
  <svg class="abs arrow" style="left:851px" width="20" height="70" viewBox="0 0 20 70"><path d="M2 0 18 35 2 70 8 35z" fill="#a9a29a"/></svg>
  <div class="abs rule" style="left:159px;top:553px;width:709px"></div>
</section>

<section class="abs about">
  <h2>Lorem ipsum dolor sit amet, consectetur adipisicing elit</h2>
  <p>Sed ut perspiciatis unde omnis iste natus error sit voluptatem accusantium doloremque laudantium, totam rem aperiam, eaque ipsa quae ab illo inventore veritatis et quasi architecto beatae vitae dicta sunt explicabo.</p>
  <span class="more-link">More <svg width="9" height="14" viewBox="0 0 9 14"><path d="M0 0 9 7 0 14z" fill="#222"/></svg></span>
</section>
<div class="abs about-tab">About Us</div>
<svg class="abs" style="left:120px;top:605px" width="18" height="12" viewBox="0 0 18 12"><path d="M0 0h18v12z" fill="#555"/></svg>

<section class="abs club">
  <h3>Join Club Tumbo</h3>
  <div class="offer">15% off on your 1st order <sup>*</sup></div>
  <div class="field">Password</div>
  <div class="btn">login</div>
  <div class="small">Forgot Password? <span class="red">Click Here</span><br>Not a member? <span class="blue">Register</span></div>
  <svg class="abs" style="left:200px;top:118px" width="100" height="100" viewBox="0 0 100 100"><circle cx="52" cy="52" r="46" fill="none" stroke="var(--red)" stroke-width="2" stroke-dasharray="6 4"/><circle cx="52" cy="52" r="40" fill="var(--red)"/></svg>
</section>

<div class="abs rule" style="left:143px;top:764px;width:626px"></div>

<section class="abs endorse">
  <div class="inner">
    <div class="panel-title">Endorsement</div>
    <div class="portrait" role="img" aria-label="Portrait of the endorsing chiropractor"></div>
    <div class="who"><b>Dr Lena Hartwell</b><i>Chiropractor &amp; Osteopath</i></div>
    <p class="quote">"Choosing the correct backpack for your child to start the school year with isan important decision for any parent to make. Importantly, your school backpack should be ergo-nomic and light to carry...</p>
    <span class="go"></span>
  </div>
</section>

<section class="abs social">
  <div class="panel-title">Our Social Networks</div>
  <svg width="220" height="100" viewBox="0 0 220 100" aria-label="Social network links">
    <g><path d="M30 92 C18 70 2 58 2 32 a28 28 0 0 1 56 0 C58 58 42 70 30 92Z" fill="#2b5fb0" stroke="#fff" stroke-width="2"/><circle cx="30" cy="31" r="18" fill="#3b74cc"/></g>
    <g transform="translate(77 0)"><path d="M30 92 C18 70 2 58 2 32 a28 28 0 0 1 56 0 C58 58 42 70 30 92Z" fill="#c8202a" stroke="#fff" stroke-width="2"/><circle cx="30" cy="31" r="18" fill="#df3942"/></g>
    <g transform="translate(154 0)"><path d="M30 92 C18 70 2 58 2 32 a28 28 0 0 1 56 0 C58 58 42 70 30 92Z" fill="#e8711e" stroke="#fff" stroke-width="2"/><circle cx="30" cy="31" r="18" fill="#f18a3a"/></g>
  </svg>
</section>

<section class="abs schools">
  <div class="inner">
    <svg width="110" height="175" viewBox="0 0 110 175"><path d="M96 0 C104 70 90 120 36 150" fill="none" stroke="#e3141b" stroke-width="9"/><path d="M20 160 44 136 50 164z" fill="#e3141b"/></svg>
    <div class="panel-title">Schools &amp; Resellers</div>
    <div class="field">Password</div>
    <div class="btn">Login</div>
    <div class="small">Forgot Password? <span class="red">Click Here</span><br>Not a Member? <span class="blue">Register</span></div>
  </div>
</section>

<footer class="abs site-footer">
  <div>Home &nbsp;|&nbsp; About Us &nbsp;|&nbsp; Kids Backpacks &nbsp;|&nbsp; Kids Bags &nbsp;|&nbsp; Sports &nbsp;|&nbsp; Arts &amp; Crafts &nbsp;|&nbsp; Kids Clothing &nbsp;|&nbsp; Music &nbsp;|&nbsp; Kids Diaries &nbsp;|&nbsp; Kids Storage &nbsp;|&nbsp; Extra Stuff &nbsp;|&nbsp; Sale &nbsp;|&nbsp; Contact</div>
  <div class="copy">Copyright Text</div>
</footer>

</body>
</html>
```